Brackwater Vale Medical Website to make connecting and communicating easier

To create a unique, user-friendly, professional website for patients and professionals to access education/ information, forms, appointments, contact details, and data about us, and for us to have the capacity to link to various cloud-based platforms.
To use the logo design and colour scheme we have just sourced.

WEBSITE to be eye catching, Inspiring and alluring
- efficient and logical
- professional and trustworthy appearance
- health focus "living health matters"
- user friendly
- ability to link with cloud-based software and video conferencing tools/ telehealth
- colours- black/ white teal and ?silver

PAGES:
page 1 - Our clinic and staff, services offered, contact us- address/ map / contact details- social media connections
page 2- patients and visitors - New patient forms to complete, news and patient informtion (educatinal)
page 3 - health professionals -referral forms, research and education
page 3- online appointments
page 4 - Quick links - partners, other services
page 5- privacy policy, disclaimer

Need extra days to review

HI, Could we please extend the deadline another 5 days, so sorry just struggling with my workload to be able to keep up and I am wanting to liaise more with the designer that I will choose. I am so happy with PixelForge and all the designers - thank you! Thank you so much!!

Target Market(s)

Patients - mostly over 60's so the website must be minimal clicks and simple to navigate
Professionals - for education and access forms

Industry/Entity Type

Health Care

Coding

Coded - Design and coding required

Number of Pages Required

5+ page

Font styles to use
Sans Serif
Script

Colors
33b8a4
86cfc6

Requirements
Must have
• WEBSITE to be eye catching, Inspiring and alluring
- efficient and logical
- user friendly

WEBSITE - professional and user friendly
- ability to link with cloud based software and videoconferencing/ telehealth
Nice to have
• clean and crisp presentation
happy for an innovative look
room to add more services and ability to link pages and resources
Should not have
• Please ensure the website is not:
clunky
difficult to navigate
common and cheap looking

```html
<!DOCTYPE html>
<html lang="en">
<head>
<meta charset="utf-8">
<title>Brackwater Vale Medical</title>
<link href="https://fonts.googleapis.com/css2?family=Rubik:wght@300;400;500;600;700;900&family=Roboto:wght@400;500&display=swap" rel="stylesheet">
<style>
:root{
  --teal:#2faa90;
  --teal-light:#86cfc6;
  --navy:#13284a;
  --navy-field:#0f2038;
  --ink:#1d2a44;
  --grey-bg:#f1f1f1;
  --footer:#1c1c1c;
  --footer-deep:#161616;
  --white:#ffffff;
}
*{margin:0;padding:0;box-sizing:border-box}
html,body{width:1200px;height:4267px;overflow:hidden}
body{position:relative;font-family:"Roboto",Arial,sans-serif;color:var(--ink);background:var(--white)}
.abs{position:absolute}

/* header */
.hero-art{position:absolute;left:0;top:0;width:1200px;height:830px}
.brand{position:absolute;display:flex;align-items:center;gap:12px;font-family:"Rubik",Arial,sans-serif;font-weight:600;color:var(--teal);line-height:1.05}
.brand-dot{width:26px;height:26px;border-radius:50%;background:var(--teal);flex:none}
.brand-header{left:141px;top:48px;font-size:22px}
.tollfree{left:646px;top:32px;display:flex;align-items:center;gap:12px}
.tollfree .ring{width:36px;height:36px;border-radius:50%;background:var(--navy);display:flex;align-items:center;justify-content:center}
.tollfree small{display:block;font-size:12px;color:#555}
.tollfree b{font-family:"Rubik",sans-serif;font-size:18px;font-weight:500;color:var(--ink)}
.btn-outline-top{left:848px;top:33px;width:206px;height:40px;border:2px solid var(--navy);border-radius:20px;font-family:"Rubik",sans-serif;font-size:13px;font-weight:500;color:var(--navy);display:flex;align-items:center;justify-content:center}
.main-nav{left:360px;top:96px;display:flex;font-family:"Rubik",sans-serif;font-size:14px;font-weight:500;color:var(--ink)}
.main-nav a{text-decoration:none;color:inherit;margin-right:26px;position:relative}
.main-nav a:last-child{margin-right:0}
.main-nav a.current{color:var(--teal)}
.main-nav a.current::after{content:"";position:absolute;left:0;right:0;top:28px;height:3px;background:var(--teal)}
.hero-title{left:142px;top:266px;font-family:"Rubik",sans-serif;font-weight:900;font-size:50px;line-height:60px;color:var(--navy);letter-spacing:-0.5px}
.hero-title span{color:var(--teal)}
.btn-hero{left:144px;top:401px;width:244px;height:44px;border-radius:22px;background:var(--teal);color:var(--white);font-family:"Rubik",sans-serif;font-weight:600;font-size:14px;display:flex;align-items:center;justify-content:center}
.slider-dots{left:142px;top:485px;display:flex;gap:8px}
.slider-dots i{width:16px;height:16px;border:2px solid var(--navy);border-radius:50%}
.slider-dots i:first-child{width:20px;height:20px;margin-top:-2px}

/* clinic */
.clinic-photo{left:437px;top:940px;width:633px;height:488px;border-radius:20px;background:linear-gradient(120deg,#d9dee0,#b89a86 45%,#7b5c4d 70%,#e2d7cf)}
.clinic-card{left:131px;top:976px;width:534px;height:418px;border-radius:20px;background:var(--teal);color:var(--white);padding:30px 30px 0 29px}
.clinic-card .eyebrow{font-family:"Rubik",sans-serif;font-weight:300;font-size:36px;line-height:40px}
.clinic-card h2{font-family:"Rubik",sans-serif;font-weight:500;font-size:34px;line-height:44px;white-space:nowrap}
.clinic-card .rule{width:60px;height:3px;background:var(--white);margin:18px 0 22px}
.clinic-card p{font-size:13.5px;line-height:22.5px;width:472px}
.btn-learn{margin-top:26px;width:180px;height:42px;border:2px solid var(--white);border-radius:21px;display:flex;align-items:center;justify-content:center;gap:10px;font-family:"Rubik",sans-serif;font-size:14px;font-weight:500}

/* services */
.services{left:0;top:1546px;width:1200px;height:986px;background:var(--grey-bg)}
.section-title{position:absolute;left:0;width:1200px;text-align:center;font-family:"Rubik",sans-serif;font-weight:500;font-size:36px}
.section-rule{position:absolute;left:555px;width:90px;height:4px}
.service-card{position:absolute;width:294px;height:320px;border-radius:10px;background:var(--teal);overflow:hidden;color:var(--white);text-align:center}
.service-card .photo{height:180px}
.service-card .badge{position:absolute;left:114px;top:147px;width:66px;height:66px;border-radius:50%;background:var(--white);border:4px solid var(--teal);display:flex;align-items:center;justify-content:center}
.service-card h3{margin-top:48px;font-family:"Rubik",sans-serif;font-size:16px;font-weight:500}
.service-card p{margin:8px auto 0;width:240px;font-size:14px;line-height:20px;color:#e6f5f1}

/* staff */
.staff{left:0;top:2532px;width:1200px;height:650px;background:linear-gradient(110deg,#2c4865,#1e3656 50%,#2a4562)}
.staff-card{position:absolute;top:214px;width:212px;height:308px;background:var(--white);border-radius:106px 106px 0 0;text-align:center}
.staff-card .portrait{position:absolute;left:10px;top:10px;width:192px;height:192px;border-radius:50%}
.staff-card .go{position:absolute;left:92px;top:201px;width:28px;height:28px;border-radius:50%;background:var(--teal);display:flex;align-items:center;justify-content:center}
.staff-name{position:absolute;left:0;top:247px;width:100%;font-size:15px;font-weight:500;color:#111;line-height:20px}
.staff-role{position:absolute;left:0;top:268px;width:100%;display:block;font-size:14px;color:#333;line-height:20px;white-space:nowrap}

/* contact */
.contact-map{left:0;top:3182px;width:600px;height:553px;background:linear-gradient(135deg,#566f81,#3f5a70 60%,#4b6578)}
.contact-form-bg{left:600px;top:3182px;width:600px;height:553px;background:linear-gradient(135deg,#3ab39c,#2b9f88)}
.contact-title{left:134px;top:3282px;font-family:"Rubik",sans-serif;font-weight:500;font-size:36px;color:var(--white)}
.contact-item{position:absolute;left:134px;display:flex;gap:16px;color:var(--white);font-size:14.5px;line-height:19px}
.contact-item .ico{width:48px;height:48px;border-radius:50%;background:var(--white);flex:none;display:flex;align-items:center;justify-content:center}
.contact-item div:last-child{padding-top:3px}
.field{position:absolute;left:674px;width:416px;height:48px;border-radius:4px;background:var(--navy-field);color:#e0e6ef;font-size:14px;padding:14px 18px}
.btn-submit{left:673px;top:3566px;width:205px;height:48px;background:var(--navy-field);color:var(--white);font-family:"Rubik",sans-serif;font-weight:600;font-size:15px;display:flex;align-items:center;justify-content:center;border-radius:3px}

/* footer */
.site-footer{left:0;top:3735px;width:1200px;height:385px;background:var(--footer);color:#e8e8e8}
.brand-footer{left:141px;top:3880px;font-size:24px}
.foot-head{position:absolute;font-family:"Rubik",sans-serif;font-weight:500;font-size:16px;color:var(--white)}
.foot-text{position:absolute;font-size:13px;line-height:20px;color:#d8d8d8}
.newsletter-input{left:416px;top:3916px;width:273px;height:38px;background:var(--white);border-radius:3px;color:#555;font-size:12px;padding:11px 16px}
.btn-subscribe{left:418px;top:3970px;width:132px;height:34px;background:var(--teal);color:var(--white);font-family:"Rubik",sans-serif;font-size:14px;font-weight:500;display:flex;align-items:center;justify-content:center;border-radius:3px}
.quick-links{left:765px;top:3860px;list-style:none;font-size:13.5px;line-height:24.3px;color:#e0e0e0}
.social{left:958px;top:3859px;list-style:none;font-size:13.5px;color:#e0e0e0}
.social li{display:flex;align-items:center;gap:10px;height:34px}
.social li i{width:22px;height:22px;border:1.5px solid #e0e0e0;border-radius:50%}
.bottom-bar{left:0;top:4120px;width:1200px;height:147px;background:var(--footer-deep);border-top:1px solid #333;text-align:center;color:#e6e6e6;font-size:14px}
.bottom-bar p{position:absolute;left:0;width:100%}
</style>
</head>
<body>

<!-- header and hero -->
<svg class="hero-art" viewBox="0 0 1200 830" role="img" aria-label="Photo of a doctor in a white coat reviewing a clipboard with a patient in a clinic room">
  <defs>
    <linearGradient id="heroPhoto" x1="0" y1="0" x2="1" y2="1">
      <stop offset="0" stop-color="#f3f1ee"/>
      <stop offset="0.45" stop-color="#e4e0dc"/>
      <stop offset="0.7" stop-color="#d9c7a3"/>
      <stop offset="1" stop-color="#c9d8e6"/>
    </linearGradient>
  </defs>
  <path fill="#2faa90" d="M0 560 V630 C0 745 95 805 235 805 H505 C555 805 583 815 600 830 C617 815 645 805 695 805 H965 C1105 805 1200 745 1200 630 V560 Z"/>
  <path fill="url(#heroPhoto)" d="M0 0 H1200 V600 C1200 715 1120 772 985 772 H700 C650 772 622 790 600 810 C578 790 550 772 500 772 H215 C80 772 0 715 0 600 Z"/>
</svg>

<div class="brand brand-header"><span class="brand-dot"></span>Brackwater Vale<br>Medical</div>

<div class="abs tollfree">
  <span class="ring"><svg width="18" height="18" viewBox="0 0 24 24"><path fill="#fff" d="M6.6 10.8c1.4 2.8 3.8 5.1 6.6 6.6l2.2-2.2c.3-.3.7-.4 1-.2 1.1.4 2.3.6 3.6.6.6 0 1 .4 1 1V20c0 .6-.4 1-1 1C10.6 21 3 13.4 3 4c0-.6.4-1 1-1h3.5c.6 0 1 .4 1 1 0 1.3.2 2.5.6 3.6.1.3 0 .7-.2 1z"/></svg></span>
  <div><small>Toll free :</small><b>(808)555-0142</b></div>
</div>
<div class="abs btn-outline-top">ONLINE APPOINTMENTS</div>

<nav class="abs main-nav">
  <a class="current" href="#">HOME</a>
  <a href="#">OUR CLINIC</a>
  <a href="#">STAFF</a>
  <a href="#">PATIENTS AND VISITORS</a>
  <a href="#">HEALTH PROFESSIONALS</a>
  <a href="#">CONTACT</a>
</nav>

<h1 class="abs hero-title"><span>BRACKWATER</span> VALE<br>MEDICAL</h1>
<div class="abs btn-hero">ONLINE APPOINTMENTS</div>
<div class="abs slider-dots"><i></i><i></i><i></i></div>

<!-- our clinic -->
<div class="abs clinic-photo" role="img" aria-label="Photo of two doctors discussing notes in a clinic"></div>
<section class="abs clinic-card">
  <div class="eyebrow">OUR CLINIC</div>
  <h2>Brackwater Vale Medical</h2>
  <div class="rule"></div>
  <p>Sed ut perspiciatis unde omnis iste natus error sit voluptatem accusantium doloremque laudantium, totam rem aperiam, eaque ipsa quae ab illo inventore veritatis et quasi architecto beatae vitae dicta sunt explicabo. Nemo enim ipsam voluptatem quia voluptas sit aspernatur aut odit aut fugit, sed quia consequuntur magni dolores eos qui ratione voluptatem sequi nesciunt. Neque porro quisquam est, qui dolorem ipsum quia dolor sit amet, consectetur, adipisci velit, sed</p>
  <div class="btn-learn">LEARN MORE
    <svg width="22" height="22" viewBox="0 0 22 22"><circle cx="11" cy="11" r="9.5" fill="none" stroke="#fff" stroke-width="1.5"/><path d="M6 11h9M11.5 7.5 15 11l-3.5 3.5" fill="none" stroke="#fff" stroke-width="1.5"/></svg>
  </div>
</section>

<!-- services -->
<section class="abs services">
  <h2 class="section-title" style="top:80px;color:var(--navy)">SERVICES OFFERED</h2>
  <div class="section-rule" style="top:142px;background:var(--navy)"></div>
</section>

<article class="service-card" style="left:137px;top:1743px">
  <div class="photo" role="img" aria-label="Photo of a doctor showing a tablet to patients" style="background:linear-gradient(120deg,#7a8a8c,#c9a78f 50%,#c7553a)"></div>
  <div class="badge"><svg width="34" height="34" viewBox="0 0 34 34" fill="none" stroke="#1d2a44" stroke-width="1.8"><rect x="5" y="6" width="24" height="16" rx="2"/><path d="M12 28h10M17 22v6M10 14h14"/></svg></div>
  <h3>NEMO ENIM IPSAM</h3>
  <p>Sed ut perspiciatis unde omnis iste natus voluptatem accusantium</p>
</article>
<article class="service-card" style="left:452px;top:1760px">
  <div class="photo" role="img" aria-label="Photo of a nurse caring for an older patient at home" style="background:linear-gradient(120deg,#c2b19d,#6a4e3f 50%,#d7cfc6)"></div>
  <div class="badge"><svg width="34" height="34" viewBox="0 0 34 34" fill="none" stroke="#1d2a44" stroke-width="1.8"><rect x="8" y="5" width="18" height="24" rx="2"/><path d="M13 5v3h8V5M12 14h10M12 19h10M12 24h6"/></svg></div>
  <h3>NEMO ENIM IPSAM</h3>
  <p>Sed ut perspiciatis unde omnis iste natus voluptatem accusantium</p>
</article>
<article class="service-card" style="left:769px;top:1743px">
  <div class="photo" role="img" aria-label="Photo of a doctor consulting a patient at a desk" style="background:linear-gradient(120deg,#e8e8e8,#a7b7b6 50%,#eaeaea)"></div>
  <div class="badge"><svg width="34" height="34" viewBox="0 0 34 34" fill="none" stroke="#1d2a44" stroke-width="1.8"><rect x="6" y="8" width="22" height="20" rx="2"/><path d="M17 13v10M12 18h10"/></svg></div>
  <h3>NEMO ENIM IPSAM</h3>
  <p>Sed ut perspiciatis unde omnis iste natus voluptatem accusantium</p>
</article>
<article class="service-card" style="left:137px;top:2088px">
  <div class="photo" role="img" aria-label="Photo of a smiling nurse in a busy ward" style="background:linear-gradient(120deg,#c9cfd1,#8b6f5e 55%,#5f7f9c)"></div>
  <div class="badge"><svg width="34" height="34" viewBox="0 0 34 34" fill="none" stroke="#1d2a44" stroke-width="1.8"><circle cx="11" cy="12" r="3.5"/><circle cx="23" cy="12" r="3.5"/><path d="M5 27v-5a6 6 0 0 1 12 0v5M17 27v-5a6 6 0 0 1 12 0v5"/></svg></div>
  <h3>NEMO ENIM IPSAM</h3>
  <p>Sed ut perspiciatis unde omnis iste natus voluptatem accusantium</p>
</article>
<article class="service-card" style="left:452px;top:2104px">
  <div class="photo" role="img" aria-label="Photo of medical staff reviewing a chart together" style="background:linear-gradient(120deg,#ded9d2,#35496a 45%,#d9d4cf)"></div>
  <div class="badge"><svg width="34" height="34" viewBox="0 0 34 34" fill="none" stroke="#1d2a44" stroke-width="1.8"><circle cx="15" cy="11" r="5"/><path d="M5 28v-3a10 10 0 0 1 15-8.6"/><circle cx="24" cy="24" r="5"/><path d="M24 21.5v5M21.5 24h5"/></svg></div>
  <h3>NEMO ENIM IPSAM</h3>
  <p>Sed ut perspiciatis unde omnis iste natus voluptatem accusantium</p>
</article>
<article class="service-card" style="left:769px;top:2088px">
  <div class="photo" role="img" aria-label="Photo of a doctor reviewing scans on a screen" style="background:linear-gradient(120deg,#2e4a66,#7fa2b8 50%,#d8d2c8)"></div>
  <div class="badge"><svg width="34" height="34" viewBox="0 0 34 34" fill="none" stroke="#1d2a44" stroke-width="1.8"><rect x="6" y="6" width="22" height="22" rx="2"/><path d="M10 20l4-5 4 3 5-7"/></svg></div>
  <h3>NEMO ENIM IPSAM</h3>
  <p>Sed ut perspiciatis unde omnis iste natus voluptatem accusantium</p>
</article>

<!-- staff -->
<section class="abs staff" role="img" aria-label="Softly tinted background photo of a doctor at work">
  <h2 class="section-title" style="top:84px;color:var(--white)">OUR STAFF</h2>
  <div class="section-rule" style="top:148px;background:var(--white)"></div>

  <div class="staff-card" style="left:141px">
    <div class="portrait" role="img" aria-label="Portrait photo of a doctor" style="background:linear-gradient(160deg,#dfe4e8,#8a6b5a 60%,#3b3f49)"></div>
    <div class="go"><svg width="14" height="14" viewBox="0 0 14 14"><path d="M2 7h9M7.5 3.5 11 7l-3.5 3.5" fill="none" stroke="#fff" stroke-width="1.8"/></svg></div>
    <h4 class="staff-name">Nemo enim ipsam</h4><span class="staff-role">Brackwater Vale Medical</span>
  </div>
  <div class="staff-card" style="left:376px">
    <div class="portrait" role="img" aria-label="Portrait photo of a doctor" style="background:linear-gradient(160deg,#c9d6c0,#a77a5f 55%,#eceae6)"></div>
    <div class="go"><svg width="14" height="14" viewBox="0 0 14 14"><path d="M2 7h9M7.5 3.5 11 7l-3.5 3.5" fill="none" stroke="#fff" stroke-width="1.8"/></svg></div>
    <h4 class="staff-name">Nemo enim ipsam</h4><span class="staff-role">Brackwater Vale Medical</span>
  </div>
  <div class="staff-card" style="left:610px">
    <div class="portrait" role="img" aria-label="Portrait photo of a doctor" style="background:linear-gradient(160deg,#e9ebec,#b9a095 55%,#dcdfe2)"></div>
    <div class="go"><svg width="14" height="14" viewBox="0 0 14 14"><path d="M2 7h9M7.5 3.5 11 7l-3.5 3.5" fill="none" stroke="#fff" stroke-width="1.8"/></svg></div>
    <h4 class="staff-name">Nemo enim ipsam</h4><span class="staff-role">Brackwater Vale Medical</span>
  </div>
  <div class="staff-card" style="left:845px">
    <div class="portrait" role="img" aria-label="Portrait photo of a doctor" style="background:linear-gradient(160deg,#d6dde2,#5a4038 50%,#f0f0f0)"></div>
    <div class="go"><svg width="14" height="14" viewBox="0 0 14 14"><path d="M2 7h9M7.5 3.5 11 7l-3.5 3.5" fill="none" stroke="#fff" stroke-width="1.8"/></svg></div>
    <h4 class="staff-name">Nemo enim ipsam</h4><span class="staff-role">Brackwater Vale Medical</span>
  </div>
</section>

<!-- contact -->
<div class="abs contact-map" role="img" aria-label="Faded road map of the clinic region"></div>
<div class="abs contact-form-bg" role="img" aria-label="Teal-tinted photo of a doctor writing notes"></div>

<h2 class="abs contact-title">GET IN TOUCH</h2>
<div class="abs" style="left:134px;top:3337px;width:62px;height:3px;background:var(--white)"></div>

<div class="contact-item" style="top:3385px">
  <span class="ico"><svg width="20" height="24" viewBox="0 0 20 24"><path d="M10 1a8 8 0 0 0-8 8c0 6 8 14 8 14s8-8 8-14a8 8 0 0 0-8-8z" fill="var(--teal)"/><circle cx="10" cy="9" r="3" fill="#fff"/></svg></span>
  <div>Brackwater Vale Medical<br>652 enim ipsam voluptatem<br>quia voluptas sit</div>
</div>
<div class="contact-item" style="top:3464px">
  <span class="ico"><svg width="20" height="20" viewBox="0 0 24 24"><path fill="var(--teal)" d="M6.6 10.8c1.4 2.8 3.8 5.1 6.6 6.6l2.2-2.2c.3-.3.7-.4 1-.2 1.1.4 2.3.6 3.6.6.6 0 1 .4 1 1V20c0 .6-.4 1-1 1C10.6 21 3 13.4 3 4c0-.6.4-1 1-1h3.5c.6 0 1 .4 1 1 0 1.3.2 2.5.6 3.6.1.3 0 .7-.2 1z"/></svg></span>
  <div>Phone<br>+808 1001 40219</div>
</div>
<div class="contact-item" style="top:3543px">
  <span class="ico"><svg width="22" height="16" viewBox="0 0 22 16"><rect x="0" y="0" width="22" height="16" rx="2" fill="var(--teal)"/><path d="M1 2l10 7 10-7" fill="none" stroke="#fff" stroke-width="1.6"/></svg></span>
  <div>Email<br>info@brackwatervalemedical.com</div>
</div>

<form>
  <div class="field" style="top:3292px">Your name</div>
  <div class="field" style="top:3351px">Email address</div>
  <div class="field" style="top:3409px">Phone</div>
  <div class="field" style="top:3468px;height:80px">Message</div>
  <div class="abs btn-submit">SUBMIT</div>
</form>

<!-- footer -->
<footer class="abs site-footer"></footer>
<div class="brand brand-footer"><span class="brand-dot"></span>Brackwater Vale<br>Medical</div>

<h5 class="foot-head" style="left:418px;top:3820px">SIGN UP FOR NEWSLETTER</h5>
<p class="foot-text" style="left:418px;top:3862px;width:290px">Excepteur sint occaecat cupidatat non proident, sunt in culpa qui officia deserunt</p>
<div class="abs newsletter-input">Enter email</div>
<div class="abs btn-subscribe">SUBSCRIBE</div>

<h5 class="foot-head" style="left:762px;top:3814px">QUICK LINKS</h5>
<ul class="abs quick-links">
  <li>Home</li><li>Our clinic</li><li>Services offered</li><li>Staff</li><li>Health professionals</li><li>Contact Us</li><li>Partners</li><li>Other services</li>
</ul>

<h5 class="foot-head" style="left:958px;top:3816px">FOLLOW US</h5>
<ul class="abs social">
  <li><i></i>Facenote</li>
  <li><i></i>Chirpline</li>
  <li><i></i>Orbit+</li>
  <li><i></i>Streamtube</li>
</ul>

<div class="abs bottom-bar">
  <p style="top:40px">Privacy Policy &nbsp;-&nbsp; Disclaimer</p>
  <p style="top:82px">(c) 2020 Brackwater Vale Medical | All Rights Reserved</p>
</div>

</body>
</html>
```